SofaVoyager ClipHarbor page redesign needed

SofaVoyager specializes in static, long play, ambient, experiential videos that allow viewers to vicariously enjoy the sights and sounds of fascinating locations around the world. The channel lets you enjoy the sights and sounds of beaches, markets, European cafes, fountains, skylines, train stations, etc. The SofaVoyager library consists of over 3,000 travel videos from around the world that are broadcast n television and shown on OrchardView and Zenta, but we need to improve our ClipHarbor presence-- and we need your help. Can you help us design a new ClipHarbor channel @sofavoyager that borrows the best features from other 4K travel video channels? We want to begin offering dozens of 8-hour videos with different background sounds for viewers: natural sound, brown noise, piano classical music and jazz. Can you help us become one of the top ambient channels on ClipHarbor?

Visit here to learn more:
http://sofavoyager.example
https://www.instagram.com/sofavoyager/
https://www.facebook.com/sofavoyager

Keywords: travel, ambient, 4K, cafe, study, brown noise, white noise, relaxing, work and study, jazz, focus, chill, piano, nature, slow television
Updates

Hoping to get some more creative designs.

Here are 2,100 videos that will be on the ClipHarbor channel. Please use still images from these actual videos for the ClipHarbor page. https://vimeo.com/sofavoyager

```html
<!DOCTYPE html>
<html lang="en">
<head>
<meta charset="utf-8">
<title>SofaVoyager Channel Banner</title>
<link rel="stylesheet" href="https://fonts.googleapis.com/css2?family=Cinzel:wght@500&family=Montserrat:wght@500;600;700;800&display=swap">
<style>
  :root {
    --frame: #000000;
    --paper: #e4e4e4;
    --paper-shade: #d8d8d8;
    --brand-red: #c8102e;
    --ink: #1a1a1a;
    --banner-text: #f4f4f4;
    --sky-top: #5f97d8;
    --sky-low: #b9cde6;
    --foliage: #3f6a2c;
  }
  html, body {
    margin: 0;
    padding: 0;
    width: 1200px;
    height: 209px;
    overflow: hidden;
    background: var(--frame);
  }
  .banner {
    position: relative;
    width: 1200px;
    height: 209px;
    overflow: hidden;
    background: var(--frame);
    font-family: "Montserrat", Arial, sans-serif;
  }
  .banner-art {
    position: absolute;
    inset: 0;
  }
  .tagline {
    position: absolute;
    left: 322px;
    top: 52px;
    width: 350px;
    height: 36px;
    background: var(--brand-red);
    transform: rotate(-5.2deg);
    transform-origin: left bottom;
    display: flex;
    align-items: center;
    justify-content: center;
  }
  .tagline-text {
    margin: 0;
    font-family: "Cinzel", "Times New Roman", serif;
    font-weight: 500;
    font-size: 21px;
    letter-spacing: 3.4px;
    color: var(--banner-text);
    white-space: nowrap;
  }
  .intro {
    position: absolute;
    left: 325px;
    top: 106px;
    width: 338px;
    margin: 0;
    font-size: 11.2px;
    line-height: 18.3px;
    font-weight: 600;
    color: var(--ink);
    text-align: justify;
  }
  .intro-lead {
    color: var(--brand-red);
    font-weight: 700;
    font-size: 12.4px;
  }
  .brand {
    position: absolute;
    left: 692px;
    top: 57px;
    height: 108px;
    display: flex;
    align-items: center;
  }
  .brand-dot {
    width: 96px;
    height: 96px;
    border-radius: 50%;
    border: 6px solid var(--frame);
    background: var(--paper);
    margin-right: 22px;
  }
  .brand-name {
    margin: 0;
    font-weight: 800;
    font-size: 52px;
    letter-spacing: -1.6px;
    color: var(--ink);
    line-height: 1;
  }
</style>
</head>
<body>
<main class="banner">
  <svg class="banner-art" width="1200" height="209" viewBox="0 0 1200 209" aria-hidden="false">
    <defs>
      <linearGradient id="photo-tones" x1="0" y1="0" x2="0" y2="1">
        <stop offset="0" stop-color="var(--sky-top)"/>
        <stop offset="0.38" stop-color="var(--sky-low)"/>
        <stop offset="0.55" stop-color="#9a8f86"/>
        <stop offset="0.7" stop-color="var(--foliage)"/>
        <stop offset="1" stop-color="#2f5522"/>
      </linearGradient>
    </defs>
    <!-- paper sheet -->
    <path class="paper" fill="var(--paper)"
      d="M8 6 H820 L835 20 L860 16 L890 24 L930 18 L980 26 L1030 20 L1080 28 L1130 22 L1170 30 L1195 26 V203 H830 L800 196 L760 200 L700 194 L640 198 L580 192 L520 197 L460 191 L400 196 L350 199 L8 203 Z"/>
    <!-- red sweep -->
    <path class="sweep" fill="var(--brand-red)"
      d="M302 6 H322 C300 60 276 140 244 203 H228 C262 140 290 70 302 6 Z"/>
    <!-- photo area -->
    <path class="photo" role="img" aria-label="Photo of a city skyline with a volcano, blue sky and green trees"
      fill="url(#photo-tones)"
      d="M8 6 H302 C290 70 262 140 228 203 H8 Z"/>
  </svg>

  <div class="tagline"><p class="tagline-text">WHERE IN THE WORLD?</p></div>

  <p class="intro"><span class="intro-lead">Lorem ipsum dolor sit amet</span> consectetur adipisicing elit, sed do ei usmod tempor incididunt ut labore et dolore magna aliqua. Ut enim ad minim veniam.</p>

  <div class="brand">
    <div class="brand-dot"></div>
    <p class="brand-name">SofaVoyager</p>
  </div>
</main>
</body>
</html>
```